International Trade Consulting Firm Seeks Quality Newsletter Design

Our company provides consulting services to Meridian 700 type companies. We compete with the largest consulting companies in the world. However, we have the highest level of expertise in the industry and need to look the most professional and high end. We have very relevant and important information to provide our customers about their compliance and projects. We will have the winning design coded to be an e-newsletter, so it needs to be one page. We want to keep our company colors and logo design in the newsletter, they are attached. We DO NOT want it to look like a mini-version of our website. We want a fresh look to this marketing piece. Newsletter will need to include title, possible sub-heading, space for a feature story, 2 other stories included, and space on either the left or right for short cuts, links or highlights of other articles. Contents/'In this issue' section, about us or branding area, section for relevant links, etc...
Target Market(s)
Meridian 700 companies, High-level management
Industry/Entity Type
Marketing

```html
<!DOCTYPE html>
<html lang="en">
<head>
<meta charset="utf-8">
<title>HLTA Newsletter — April 2014</title>
<link rel="stylesheet" href="https://fonts.googleapis.com/css2?family=Lato:ital,wght@0,400;0,700;0,900;1,700;1,900&display=swap">
<style>
  :root{
    --ink:#1a1718;
    --masthead:#231f20;
    --brand-green:#0f9a4a;
    --brand-cream:#e9e4a6;
    --headline-green:#2e7d0c;
    --body-green:#b3cb5a;
    --sidebar-yellow:#e9ef62;
    --issue-lime:#bff00b;
    --issue-teal:#17a39b;
    --white:#ffffff;
  }
  *{box-sizing:border-box;margin:0;padding:0}
  html,body{width:931px;height:1200px;overflow:hidden;background:var(--white)}
  body{font-family:"Lato",sans-serif;color:var(--ink);position:relative}

  .masthead{position:absolute;left:22px;top:10px;width:877px;height:178px;background:var(--masthead)}
  .brand{position:absolute;left:18px;top:52px;display:flex;align-items:center;gap:10px}
  .brand-mark{width:14px;height:14px;background:var(--brand-green)}
  .brand-name{font-weight:900;font-size:19px;line-height:1.15;letter-spacing:1px;color:var(--brand-green);text-transform:uppercase}
  .title-art{position:absolute;left:283px;top:12px;width:528px;height:148px;border-radius:10px;
    background:linear-gradient(90deg,#f0b63a 0%,#b5566a 30%,#c9d86a 60%,#ee8a6a 100%)}
  .issue-meta{position:absolute;top:158px;font-size:15px;color:var(--brand-cream)}
  .meta-vol{left:288px}.meta-date{left:511px}.meta-price{left:741px}

  .page{position:absolute;left:22px;top:188px;width:877px;height:745px;background:var(--body-green)}
  .sidebar-heading{position:absolute;left:8px;top:26px;width:270px;font-size:26px;line-height:1.25;font-weight:400}
  .sidebar{position:absolute;left:0;top:105px;width:280px;height:640px;background:var(--sidebar-yellow);padding:14px 2px 0 2px}
  .headline{position:absolute;left:300px;top:22px;font-size:72px;font-weight:700;line-height:90px;color:var(--headline-green);letter-spacing:.5px;white-space:nowrap}

  .story p{font-size:15px;line-height:19.5px;text-indent:17px}
  .story p.lead{text-indent:0}
  .dropcap{float:left;font-weight:900;font-size:60px;line-height:46px;margin:2px 6px 0 0}
  .col-main{position:absolute;left:300px;top:206px;width:280px}
  .col-side{position:absolute;left:598px;top:206px;width:280px}

  .contents-band{position:absolute;left:22px;top:933px;width:877px;height:70px;background:var(--issue-lime)}
  .contents-title{position:absolute;left:198px;top:3px;font-weight:900;font-size:28px;line-height:28px;letter-spacing:-.5px}
  .contents-title em{display:block;color:var(--issue-teal);font-style:italic;margin-left:38px;font-size:36px;line-height:36px}
  .contents{position:absolute;left:22px;top:1003px;width:578px;height:195px;background:var(--body-green)}
  .contents-aside{position:absolute;left:600px;top:1003px;width:299px;height:195px;background:var(--sidebar-yellow)}
  .contents-item{position:absolute;left:26px;width:540px;font-weight:700;font-style:italic;font-size:21px;line-height:29px}
  .contents-item .page-ref{position:absolute;top:0;font-style:italic}
</style>
</head>
<body>
  <header class="masthead">
    <div class="brand"><span class="brand-mark"></span><span class="brand-name">Harborline<br>Trade Advisors</span></div>
    <div class="title-art" role="img" aria-label="Decorative patterned title lettering"></div>
    <span class="issue-meta meta-vol">VOL. 1</span>
    <span class="issue-meta meta-date">APRIL 2014</span>
    <span class="issue-meta meta-price">$5.00</span>
  </header>

  <main class="page">
    <h2 class="sidebar-heading">Viris legere periculis ad vim iruditi</h2>
    <aside class="sidebar story">
      <p class="lead"><span class="dropcap">E</span>t audiam torquatos concludaturque nec, et vel inermis similique. Sea ex tibique electram sapientem, possit volumus qui an, in copiosae indoctum quaerendum cum. Eirmod eripuit scribentur at mel, nobis copiosae eam at. Ex tale gubergren pro, cum et lorem democritum, duo justo dolore et. Aliquip copiosae no vim. Veri nulla harum sed te, phaedrum adversarium disputationi et pro, nam eu mnesarchum voluptatum.</p>
      <p>Viris legere periculis ad vim, in facer eruditi ius. Purto debet consectetuer ad vim, pro ut illud quidam, te est facete melius. An ius quod tollit, quo ei congue nostro, in vim dolorum suavitate.</p>
      <p class="lead">Eu mea velit veritus, ei veri explicari appellantur has. Ad tollit splendide assentior vix, no sit tation iuvaret corpora.</p>
      <p>Ludico scripta ex vix, scripta nostrud vel te. Mea vivendo corrumpit gubergren at, no novum saepe postulant vim. Cum ut scaevola reprehendunt, vix ne hendrerit neglegentur, liber erant libris ad mei. Ut est dicam aliquam fastidii.</p>
      <p>Suscipit copiosae definiebas mel in, eu eam magna legere. Et epicurei appareat suscipiantur mea.</p>
    </aside>

    <h1 class="headline">LOREM IPSUM<br>MISA CANTADA</h1>

    <article class="col-main story">
      <p class="lead"><span class="dropcap">L</span>orem ipsum dolor sit amet, vis elitr vidisse no, sensibus salutatus at sed. Vis reprehendunt vituperatoribus ea, dicam viderer eruditi ei qui. Doctus expetenda mea te. Pri ea mnesarchum conclusionemque, amet evertitur no vim. Per mazim minimum et, vim iudico lucilius nominati id, eu his autem sanctus instructior. Mei justo intellegam no.</p>
      <p>Eum ei sint case decore, nam te modus forensibus scripserit. No nec nisl primis, nostrud habemus tibique at pro. Et sed nostrum facilisi legendos. In placerat mediocrem pri, ex cotidieque instructior pro.</p>
      <p>Duo in choro malorum, mucius inermis probatus eam te. Usu ne eripuit numquam similique, duo ea scaevola comprehensam, ne ridens quodsi cum. Quaeque oportere et sit, pro vocibus nostrum vituperata ea. Mel erant sensibus et, at suscipit postulant est. Duo ad utinam verterem, ex mei summo maiestatis, iusto perpetua qui cu. Pri eu alterum dissentiet.</p>
    </article>

    <article class="col-side story">
      <p>At ferri complectitur has. At vel idque impedit accusam. Ne vel alii iuvaret oportere, at erat maluisset vix, no sea justo atqui vivendo.</p>
      <p class="lead">At mel aliquip probatus, equidem dignissim abhorreant te has, justo graeco indoctum an vim. Ut scribentur delicatissimi quo, dolore mollis deleniti ne vim, ne duo summo iisque constituto. Ad soluta senserit cotidieque vis.</p>
      <p>Lorem ipsum dolor sit amet, vis elitr vidisse no, sensibus salutatus at sed. Vis reprehendunt vituperatoribus ea, dicam viderer eruditi ei qui. Doctus expetenda mea te. Pri ea mnesarchum conclusionemque, amet evertitur no vim. Per mazim minimum et, vim iudico lucilius nominati id, eu his autem sanctus instructior. Mei justo intellegam no.</p>
      <p>Et audiam torquatos concludaturque nec, et vel inermis similique. Sea ex tibique electram sapientem, possit volumus qui an, in copiosae indoctum quaerendum cum. Eirmod eripuit scribentur at mel, nobis.</p>
    </article>
  </main>

  <section class="contents-band">
    <h3 class="contents-title">IN THIS<em>ISSUE</em></h3>
  </section>
  <nav class="contents">
    <div class="contents-item" style="top:12px">Vis reprehendunt vituperatoribus ea<span class="page-ref" style="left:454px">P.2</span></div>
    <div class="contents-item" style="top:55px">Suscipit copiosae definiebas mel in,<br>eu eam magna legere<span class="page-ref" style="left:448px;top:29px">P.4</span></div>
    <div class="contents-item" style="top:120px">Mea vivendo corrumpit gubergren<br>at, no novum saepe postulant vim<span class="page-ref" style="left:454px;top:29px">P.3</span></div>
  </nav>
  <div class="contents-aside"></div>
</body>
</html>
```